Design a Flyer for Tennis Coaching

I need a flyer designed. One sided A5 size and I would like the editable files (so that I can update prices/info in future). Relevent content is attached in word doc.

```html
<!DOCTYPE html>
<html lang="en">
<head>
<meta charset="utf-8">
<title>Tennis Lessons Flyer</title>
<link href="https://fonts.googleapis.com/css2?family=Open+Sans:wght@400;600;700;800&display=swap" rel="stylesheet">
<style>
:root{
  --blue-deep:#0c4784;
  --blue-mid:#1a64a6;
  --blue-light:#2f80c4;
  --orange:#f5a31a;
  --orange-dark:#ec7f12;
  --pink:#e6336f;
  --white:#ffffff;
  --text-soft:#e9f1fa;
  --logo-ink:#4d6f8f;
}
*{margin:0;padding:0;box-sizing:border-box}
html,body{width:846px;height:1200px;overflow:hidden;background:var(--blue-deep)}
body{font-family:"Open Sans",Arial,sans-serif;color:var(--white)}
.flyer{position:relative;width:846px;height:1200px;overflow:hidden;
  background:linear-gradient(180deg,var(--blue-mid) 0%,var(--blue-deep) 55%,#093b70 100%)}
.hero{position:absolute;left:0;top:0;width:846px;height:560px}
.brand{position:absolute;right:0;top:0;width:250px;height:165px;background:var(--white);
  border-bottom-left-radius:60px;display:flex;align-items:center;justify-content:center;gap:10px}
.brand-dot{width:22px;height:22px;border-radius:50%;background:var(--logo-ink)}
.brand-name{font-weight:700;font-size:34px;color:var(--logo-ink);font-family:"Open Sans",Arial,sans-serif}
.highlights{position:absolute;left:457px;top:370px;width:366px;height:193px;background:var(--pink);
  border-radius:14px;padding:14px 20px;list-style:none;box-shadow:0 4px 10px rgba(0,0,0,.25)}
.highlights li{font-size:17.5px;font-weight:600;padding:8px 0 8px 24px;position:relative;
  border-bottom:1px dashed rgba(255,255,255,.55)}
.highlights li:last-child{border-bottom:none}
.highlights li::before{content:"";position:absolute;left:2px;top:15px;border-left:9px solid var(--white);
  border-top:5px solid transparent;border-bottom:5px solid transparent;opacity:.9}
.title{position:absolute;left:39px;top:522px;font-size:44px;font-weight:600;letter-spacing:1px;
  text-shadow:0 3px 5px rgba(0,0,0,.45)}
.intro{position:absolute;left:36px;top:584px;width:780px;font-size:15.2px;line-height:21px;color:var(--text-soft)}
.section-head{position:absolute;left:36px;top:697px;font-size:21px;font-weight:600}
.kids-photo{position:absolute;left:36px;top:730px;width:261px;height:167px;border:4px solid #6fa6d6;
  background:linear-gradient(160deg,#9ec7e6 0%,#e8c2a6 35%,#f0d2b8 55%,#3a4b5c 85%,#1f2a33 100%)}
.program{position:absolute}
.program h3{font-size:25px;font-weight:700;letter-spacing:.5px}
.program h3 span{font-size:16px;font-weight:400;letter-spacing:0}
.program p{font-size:16.2px;line-height:23px;color:var(--text-soft)}
.red{left:327px;top:714px;width:500px}
.orange{left:322px;top:808px;width:510px}
.green{left:36px;top:916px;width:500px}
.blue{left:36px;top:1038px;width:500px}
.green p,.blue p{width:490px}
.divider{position:absolute;left:556px;top:928px;width:1px;height:218px;background:rgba(255,255,255,.55)}
.contact{position:absolute;left:578px;top:944px;width:250px}
.contact h4{font-size:20px;font-weight:700;margin-bottom:10px}
.contact-row{display:flex;align-items:center;gap:12px;margin-bottom:8px}
.contact-row svg{flex:none}
.contact-row.phone{font-size:25px;font-weight:600}
.contact-row.address{font-size:17px;line-height:23px;align-items:flex-start}
.contact-row.email{font-size:16px}
.website{position:absolute;left:0;top:1160px;width:846px;text-align:center;font-size:19px;font-weight:600}
</style>
</head>
<body>
<div class="flyer">
  <svg class="hero" viewBox="0 0 846 560" aria-hidden="false">
    <defs>
      <linearGradient id="photoTone" x1="0" y1="0" x2="1" y2="1">
        <stop offset="0" stop-color="#8fb7d6"/>
        <stop offset=".3" stop-color="#e9d2bd"/>
        <stop offset=".55" stop-color="#f3ede6"/>
        <stop offset="1" stop-color="#6f9cc4"/>
      </linearGradient>
      <linearGradient id="orangeBand" x1="0" y1="0" x2="1" y2="0">
        <stop offset="0" stop-color="var(--orange)"/>
        <stop offset="1" stop-color="var(--orange-dark)"/>
      </linearGradient>
    </defs>
    <rect x="0" y="0" width="846" height="500" fill="url(#photoTone)" role="img" aria-label="Photo of a smiling young girl in a tennis shirt holding a racquet"/>
    <path d="M0,320 C240,350 540,410 846,385 L846,440 C540,470 240,420 0,372 Z" fill="#ffffff"/>
    <path d="M0,345 C250,385 560,450 846,425 L846,495 C560,505 250,455 0,425 Z" fill="url(#orangeBand)"/>
    <path d="M0,418 C250,462 560,520 846,488 L846,560 L0,560 Z" fill="var(--blue-mid)"/>
  </svg>

  <div class="brand">
    <span class="brand-dot"></span>
    <span class="brand-name">Courtside</span>
  </div>

  <ul class="highlights">
    <li>Group and Private Lessons</li>
    <li>5 year olds to Adults</li>
    <li>After School and Saturday Mornings</li>
    <li>Competition Tennis</li>
  </ul>

  <h1 class="title">TENNIS LESSONS</h1>
  <p class="intro">Mark Delaney is fully qualified through National Tennis Council and holds Bachelors and Masters Degrees in Sports Education. Following a successful overseas coaching career he has now been coaching at Ellis Park Reserve for the past 24 years. He oversees a small team of enthusiastic coaches who make sure that every student is successful and enjoys their lessons.</p>

  <h2 class="section-head">COACHING PROGRAM:</h2>
  <div class="kids-photo" role="img" aria-label="Photo of two young girls leaning on a tennis net holding a ball"></div>

  <div class="program red">
    <h3>RED PROGRAM <span>&nbsp;- ages 5-7 years</span></h3>
    <p>Maximum of 4 students in a 30 minutes class.<br>Students learn the basics in a fun, game based lesson.</p>
  </div>
  <div class="program orange">
    <h3>ORANGE PROGRAM<span>- ages 8-9 years</span></h3>
    <p>Maximum of 3 students in a 30 minute lesson or 6 students in a one hour lesson. Focus is on developing effective technique and being able to apply it in game situations.</p>
  </div>
  <div class="program green">
    <h3>GREEN PROGRAM <span>– ages 10-18 years</span></h3>
    <p>2 students for 30 minutes or 4 students in a one hour class. More advanced techniques are learned as well as match-play procedures and strategy.</p>
  </div>
  <div class="program blue">
    <h3>BLUE PROGRAM <span>- Private lessons (any age)</span></h3>
    <p>Individualised instruction leads to the fastest progress. Private lessons are the choice of our keenest as well as our more advanced students.</p>
  </div>

  <div class="divider"></div>
  <div class="contact">
    <h4>CONTACT DETAILS:</h4>
    <div class="contact-row phone">
      <svg width="20" height="20" viewBox="0 0 24 24" aria-hidden="true"><path fill="#fff" d="M3 8c0-3 4-4 9-4s9 1 9 4v2h-5V8c-1-.6-2.5-.8-4-.8S9 7.4 8 8v2H3z"/><rect x="6" y="12" width="12" height="8" rx="1.5" fill="#fff"/><circle cx="12" cy="16" r="2" fill="var(--blue-deep)"/></svg>
      <span>9555 0182</span>
    </div>
    <div class="contact-row phone">
      <svg width="20" height="20" viewBox="0 0 24 24" aria-hidden="true"><path fill="#fff" d="M6.6 10.8a15 15 0 0 0 6.6 6.6l2.2-2.2c.3-.3.7-.4 1-.2 1.1.4 2.3.6 3.6.6.6 0 1 .4 1 1V20c0 .6-.4 1-1 1A17 17 0 0 1 3 4c0-.6.4-1 1-1h3.5c.6 0 1 .4 1 1 0 1.3.2 2.5.6 3.6.1.3 0 .7-.2 1z"/></svg>
      <span>0400 123 987</span>
    </div>
    <div class="contact-row address">
      <svg width="20" height="24" viewBox="0 0 24 24" aria-hidden="true"><path fill="#fff" d="M12 2a7 7 0 0 0-7 7c0 5 7 13 7 13s7-8 7-13a7 7 0 0 0-7-7zm0 9.5A2.5 2.5 0 1 1 12 6.5a2.5 2.5 0 0 1 0 5z"/></svg>
      <span>Ellis Park Reserve,<br>Ridgewood Hills</span>
    </div>
    <div class="contact-row email">
      <svg width="20" height="16" viewBox="0 0 24 18" aria-hidden="true"><rect x="1" y="1" width="22" height="16" fill="none" stroke="#fff" stroke-width="2"/><path d="M1 1l11 9 11-9" fill="none" stroke="#fff" stroke-width="2"/></svg>
      <span>mark@rallypoint.example</span>
    </div>
  </div>

  <div class="website">www.rallypoint.example</div>
</div>
</body>
</html>
```